Fire Alarm and Access Control Permit Drawings

My company engineers and designs fire alarm and access control drawings for companies that install these type systems in commercial office buildings. We want a post card mailer to go out to all fire alarm and security companies in Texas. We want companies to outsource their fire alarm and access control drawings to us. We do submittal, as-built and permit drawings specific to the security and fire alarm industry. Our price list is on the web site at www.hvrplanworks.com/pricelist.html.
Here is a good example of words to use:
"HVR Plan Works specializes in submittal, as-built and permit drawings for the commercial fire alarm and access control industry. We prepare and submit plans on your behalf to jurisdictions and consultants all over Texas. Give us a call today!"

Target Market(s)

Commercial fire alarm and security integrators who currently do their drawings in-house or through a 3rd party like us.

Industry/Entity Type

Security

Requirements
Must have
• Must have front and back side with room for addressing, must have our web address, physical address and phone number. State on the post card to contact Colin Marwick for more information or questions.

www.hvrplanworks.com

2718 Quarrington Street
Suite 342
Houston, Texas 77418
Nice to have
• We like the look and feel of building floor plans on a desk or rolled up with drafting tools. But we do not want to convey that we hand-draw our plans. Everything we do is drawn in AutoCAD.
Nice to have a link to our web site or reference to the pricelist being on the web site. www.hvrplanworks.com/pricelist.html.
Should not have
• Don't be too wordy.

```html
<!DOCTYPE html>
<html lang="en">
<head>
<meta charset="utf-8">
<title>HVR Plan Works – Postcard Mailer</title>
<link rel="stylesheet" href="https://fonts.googleapis.com/css2?family=Courgette&family=Marcellus+SC&family=Oswald:wght@500;600&family=PT+Sans:wght@700&family=Roboto+Condensed:wght@400;700&family=Roboto:wght@300;400&display=swap">
<style>
  :root {
    --backdrop: #a9a9ab;
    --navy: #1f2a5e;
    --blue: #2f5fb9;
    --blue-deep: #1d3c86;
    --ink: #1b1b1b;
    --grey-bar: #8e8f92;
    --charcoal: #4a4b4f;
    --paper: #ffffff;
    --paper-back: #f3f3f5;
    --script-blue: #2a4c9e;
    --soft-text: #dfe6f5;
  }
  * { margin: 0; padding: 0; box-sizing: border-box; }
  html, body {
    width: 1200px;
    height: 1098px;
    overflow: hidden;
    background: var(--backdrop);
  }
  .canvas { position: relative; width: 1200px; height: 1098px; }
  .postcard {
    position: absolute;
    left: 31px;
    width: 633px;
    height: 491px;
    display: block;
  }
  .postcard--front { top: 47px; }
  .postcard--back { top: 563px; }

  .brand-name { font-family: "Roboto Condensed", sans-serif; font-weight: 700; font-size: 33px; fill: var(--navy); }
  .pitch { font-family: "Roboto Condensed", sans-serif; font-size: 15.5px; fill: var(--ink); }
  .pitch-script { font-family: "Courgette", cursive; font-size: 13.5px; fill: var(--script-blue); }
  .address-line { font-family: "Roboto Condensed", sans-serif; font-size: 17px; fill: var(--ink); }
  .web-line { font-family: "Roboto Condensed", sans-serif; font-size: 14px; fill: #fff; letter-spacing: 0.3px; }
  .contact-line { font-family: "Roboto", sans-serif; font-weight: 300; font-size: 17.5px; fill: var(--soft-text); }
  .cta { font-family: "Oswald", sans-serif; font-weight: 600; font-size: 19px; fill: #fff; letter-spacing: 1px; }
  .cta-phone { font-family: "Oswald", sans-serif; font-weight: 500; font-size: 20px; fill: #fff; letter-spacing: 1px; }

  .postage-label { font-family: "Roboto", sans-serif; font-size: 21px; fill: #000; }
  .back-web { font-family: "Marcellus SC", serif; font-size: 12.5px; fill: var(--navy); letter-spacing: 0.4px; }
  .back-copy { font-family: "Marcellus SC", serif; font-size: 13.5px; fill: var(--ink); letter-spacing: 0.4px; }
  .back-phone { font-family: "Marcellus SC", serif; font-size: 18px; fill: var(--ink); }
  .price-note { font-family: "PT Sans", sans-serif; font-weight: 700; font-size: 8px; fill: var(--ink); }
</style>
</head>
<body>
<main class="canvas">

  <!-- Front of the mailer -->
  <svg class="postcard postcard--front" viewBox="0 0 577 447" xmlns="http://www.w3.org/2000/svg" aria-label="Postcard front">
    <defs>
      <linearGradient id="photo-tones" x1="0" y1="0" x2="1" y2="1">
        <stop offset="0" stop-color="#d9dadc"/>
        <stop offset="0.45" stop-color="#c9b9a4"/>
        <stop offset="0.7" stop-color="#b27a45"/>
        <stop offset="1" stop-color="#8d8f94"/>
      </linearGradient>
      <linearGradient id="band-blue" x1="0" y1="0" x2="0" y2="1">
        <stop offset="0" stop-color="#3466c2"/>
        <stop offset="0.55" stop-color="var(--blue-deep)"/>
        <stop offset="1" stop-color="var(--navy)"/>
      </linearGradient>
    </defs>

    <rect class="card-surface" width="577" height="447" fill="var(--paper)"/>
    <polygon class="corner-accent" points="477,0 577,0 577,100" fill="var(--navy)"/>

    <!-- Brand mark -->
    <g class="brand">
      <rect x="14" y="52" width="58" height="58" rx="6" fill="var(--blue)"/>
      <text class="brand-name" x="84" y="93">HVR Plan Works</text>
    </g>

    <!-- Hero image area -->
    <polygon class="header-rule" points="0,116 318,116 322,124 0,124" fill="var(--navy)"/>
    <polygon class="hero-photo" role="img" aria-label="Photo of architectural floor plans on a desk with a timber house frame, brick wall, protractor and ruler"
             points="0,124 322,124 452,308 0,370" fill="url(#photo-tones)"/>

    <!-- Pitch copy -->
    <g class="pitch-block" transform="translate(346,92) rotate(-30)">
      <text class="pitch" x="0" y="0">HVR Plan Works</text>
      <text class="pitch" x="0" y="18">specializes in submittal,</text>
      <text class="pitch" x="0" y="36">as-built and permit</text>
      <text class="pitch" x="0" y="54">drawings for the</text>
      <text class="pitch" x="0" y="72">commercial fire alarm and</text>
      <text class="pitch" x="0" y="90">access control industry.</text>
    </g>
    <g class="pitch-script-block" transform="rotate(-6 560 220)" text-anchor="end">
      <text class="pitch-script" x="560" y="192">We prepare and</text>
      <text class="pitch-script" x="560" y="209">submit plans on your</text>
      <text class="pitch-script" x="560" y="226">behalf to jurisdictions</text>
      <text class="pitch-script" x="560" y="243">and consultants all</text>
      <text class="pitch-script" x="560" y="260">over Texas.</text>
    </g>

    <!-- Blue call-to-action band -->
    <polygon class="cta-band" points="0,380 470,316 577,250 577,447 0,447" fill="url(#band-blue)"/>

    <!-- Address strips -->
    <g class="address-strips" transform="rotate(-8 0 360)">
      <rect x="-20" y="336" width="500" height="27" fill="var(--grey-bar)"/>
      <text class="address-line" x="8" y="356">2718 QUARRINGTON STREET, SUITE 342, HOUSTON, TEXAS 77418</text>
      <rect x="285" y="363" width="196" height="22" fill="var(--charcoal)"/>
      <text class="web-line" x="298" y="379">WWW.HVRPLANWORKS.COM</text>
    </g>

    <g class="contact" text-anchor="middle">
      <text class="contact-line" x="162" y="389">Contact Colin Marwick for</text>
      <text class="contact-line" x="162" y="413">more information or questions</text>
    </g>
    <text class="cta" x="297" y="389">GIVE US A CALL TODAY!</text>
    <text class="cta-phone" x="327" y="416">713.555.0148</text>
    <g class="phone-icon" transform="translate(472,401)">
      <rect width="14" height="14" rx="3" fill="#9aa0ab"/>
      <path d="M4.2 3 L6 3 L6.6 5.4 L5.5 6.3 C6 7.4 6.7 8.2 7.7 8.6 L8.6 7.5 L11 8.1 L11 9.9 C11 10.6 10.4 11 9.8 11 C6.3 10.7 3.4 7.8 3.1 4.2 C3.1 3.6 3.5 3 4.2 3 Z" fill="#3c4250"/>
    </g>
  </svg>

  <!-- Back of the mailer -->
  <svg class="postcard postcard--back" viewBox="0 0 577 447" xmlns="http://www.w3.org/2000/svg" aria-label="Postcard back">
    <rect class="card-surface" width="577" height="447" fill="var(--paper-back)"/>
    <polygon class="corner-accent" points="0,0 97,0 0,77" fill="var(--navy)"/>

    <g class="postage-box">
      <rect x="437.5" y="15.5" width="124" height="127" fill="#fff" stroke="#000" stroke-width="1"/>
      <text class="postage-label" x="499.5" y="86" text-anchor="middle">POSTAGE</text>
    </g>

    <line class="address-divider" x1="279" y1="167" x2="279" y2="295" stroke="#555" stroke-width="1"/>

    <g class="back-details">
      <text class="back-web" x="73" y="166">WWW.HVRPLANWORKS.COM</text>
      <text class="back-copy" x="73" y="196">for more information</text>
      <text class="back-copy" x="73" y="221">or questions,</text>
      <text class="back-copy" x="73" y="246">Contact</text>
      <text class="back-copy" x="73" y="270">Colin Marwick on</text>
      <text class="back-phone" x="73" y="297">713.555.0148</text>
      <circle cx="71.5" cy="320" r="1.6" fill="var(--ink)"/>
      <text class="price-note" x="74" y="328">HVR Price List: www.hvrplanworks.com/pricelist.html</text>
    </g>
  </svg>

</main>
</body>
</html>
```